Spiritual Self-Help Book Cover: The Path of RISING the Heart Weaver

I’m looking for a powerful, eye-catching, and soulfully designed book cover for my upcoming spiritual self-help book titled: “The Path of RISING the Heart Weaver: A Quiet Path of Finding Your Voice, Honoring Your Flame, and Living Your Calling.” by Mira Holtby

Trim size: 6 x 9 inches (15.24 x 22.86 cm), full wrap cover including front, back, and spine.

This book is for spiritually awakening readers who are navigating inner transformation and want to reclaim their truth and power. The word BECOMING should stand out the most in the title design, as this is the central theme of the book — it’s a journey of evolution and embodiment.
I'm looking for a design that feels expansive, sacred, mystical, and empowering, with a tone that blends feminine spiritual energy with grounded strength. It should appeal to those interested in energy healing, light language, emotional alchemy, and soul purpose.

Design elements can include things like light, energy fields, sacred geometry, cosmic or mystical elements, or anything that visually conveys transformation, inner alchemy, or divine remembrance. Nothing too dark or overly esoteric — it should feel inspiring and elevated.
The final book will be available in print and ebook formats, so the design needs to be high resolution and adaptable.

Design Inspirations / Visual Keywords:
I’m drawn to covers that evoke a sense of spiritual awakening, inner transformation, and cosmic remembrance. Some elements I love include:
- Light bursts, energy waves, sacred geometry, subtle gold or white light effects
- Ethereal yet grounded designs (think: not overly abstract, but mystical and refined)
- Fonts that feel elevated, clean, and spacious, not overly bold or rigid
Please avoid designs that feel too dark, heavy, overly masculine, or sci-fi. I want the reader to feel empowered, uplifted, and activated the moment they see the cover.
- Final deliverables must include the original editable source file—preferably PSD (Photoshop)—so I can make future updates, including a German version of the book.

Back Cover Copy:
You were never broken—only buried beneath the layers of who you thought you had to be.
The Path of RISING the Heart Weaver is not just a book—it’s a sacred activation. A companion for the seeker who’s always felt like there was more. A map for those who are ready to transcend limitation, shed old identities, and reclaim the radiance of their true essence.
This isn’t about becoming something new. It’s about remembering what has always lived within you.
Through powerful transmissions, energetic teachings, and soul-deep reflection, you’ll be guided to awaken your inner Soul Alchemist—the version of you who lives in deep integrity with your truth, leads from embodied frequency, and walks as a living portal for transformation.
If you’ve felt the call to step into a higher path, this is your invitation.
The alchemical path awaits.

About the Author:
Mira Holtby is a Soul Alchemist, Light Language Channel, and transformational guide for awakening souls on the path of ascension and embodiment. Through her transmissions, activations, and deeply alchemical teachings, she supports others in dissolving limitations and becoming the living transmission of their soul’s truth. Her work empowers others to become the Soul Alchemist of their own life—fully awakened, energetically aligned, and consciously creating their reality from within.

Spine Text:
The Path of RISING the Heart Weaver Mira Holtby

Other Notes:
Please ensure the back cover layout includes space for:
• Barcode (bottom right or bottom center, standard placement)
• Optional decorative accents that match the front cover design
• Flow and visual balance across the full wrap (front + spine + back)

I uploaded a AI generated image that really captures the energy and feeling I’m going for—vibrant, mystical, intuitive, radiant, and feminine. I’m looking for designs that evoke soul embodiment, sacred transformation, and energetic activation like this. Please feel free to explore similar colors and tones.

Target Market(s)

Spiritually awakening women (and men) ages 30–55 who are seeking deeper truth, emotional healing, energetic expansion, and soul embodiment. They’re interested in spiritual growth, light language, quantum manifestation, energy work, and the journey of becoming their highest self.

Industry/Entity Type

Books / Publishing / Spirituality / Personal Development

Font styles to use
Serif
Script

Colors
A7469A
B969AE
D3A5CF
EDDBEB
F8F0F9
6B429C
8869AF
B7A5CE
E3DAEB
F3F0F8

Requirements
Must have
• Title: The Path of RISING the Heart Weaver (The word BECOMING should visually stand out the most) Subtitle: A Sacred Journey of Reclaiming Your Power, Remembering Your Light, and Embodying Your Truth. Author name Mira Holtby. Mystical yet grounded imagery (light, sacred geometry, ethereal elements) Energetic or spiritual theme (divine remembrance, embodiment, inner alchemy) High-resolution design adaptable for both print and ebook
Nice to have
• Subtle gold, white, or light-infused accents Cosmic or celestial textures (not heavy space imagery, but gently divine) Feminine and refined feel (without being overly soft or passive) A sense of spaciousness and radiance
Should not have
• Designs that feel dark, heavy, harsh, or overly masculine Sci-fi or overly abstract illustrations Bold, rigid fonts or clunky layout Imagery that feels disconnected from emotional or spiritual resonance

```html
<!DOCTYPE html>
<html lang="en">
<head>
<meta charset="utf-8">
<title>Spiritual Self-Help Book Cover: The Path of RISING the Heart Weaver</title>
<link rel="stylesheet" href="https://fonts.googleapis.com/css2?family=Cinzel:wght@500;600&family=Pinyon+Script&family=Noto+Serif:ital@1&display=swap">
<style>
  :root {
    --page: #ffffff;
    --night: #2a2350;
    --violet-deep: #4e2d7e;
    --violet: #6b429c;
    --orchid: #a7469a;
    --lilac: #b969ae;
    --blush: #d3a5cf;
    --gold: #ffe3a0;
    --gold-core: #fff6d8;
    --ink-author: #34195a;
    --ink-light: #ffffff;
  }
  * { margin: 0; padding: 0; box-sizing: border-box; }
  html, body {
    width: 1200px;
    height: 1200px;
    overflow: hidden;
    background: var(--page);
  }
  .book-cover {
    position: absolute;
    left: 240px;
    top: 60px;
    width: 720px;
    height: 1080px;
    overflow: hidden;
    text-align: center;
  }
  .cover-art {
    position: absolute;
    inset: 0;
    background:
      radial-gradient(ellipse 46% 30% at 50% 26%, var(--gold-core) 0%, var(--gold) 22%, rgba(255, 200, 150, 0.55) 48%, rgba(220, 150, 190, 0) 80%),
      radial-gradient(ellipse 70% 45% at 50% 55%, rgba(211, 165, 207, 0.75) 0%, rgba(185, 105, 174, 0.35) 55%, rgba(185, 105, 174, 0) 100%),
      linear-gradient(180deg, var(--night) 0%, #5a4a86 16%, #b07eae 36%, #b67cb3 52%, var(--lilac) 64%, var(--violet) 84%, var(--violet-deep) 100%);
  }
  .author-name {
    position: absolute;
    top: 46px;
    left: 0;
    right: 0;
    font-family: "Cinzel", serif;
    font-weight: 500;
    font-size: 60px;
    letter-spacing: 3px;
    color: var(--ink-author);
    line-height: 1;
  }
  .title {
    position: absolute;
    left: 0;
    right: 0;
    top: 600px;
    color: var(--ink-light);
    text-shadow: 0 2px 10px rgba(70, 30, 100, 0.35);
  }
  .title-script {
    display: block;
    font-family: "Pinyon Script", cursive;
    font-weight: 400;
    line-height: 1;
  }
  .title-lead { font-size: 84px; }
  .title-key {
    display: block;
    font-family: "Cinzel", serif;
    font-weight: 500;
    font-size: 104px;
    letter-spacing: 2px;
    line-height: 1;
    margin-top: 4px;
  }
  .title-join { font-size: 82px; margin-top: 0; }
  .title-name {
    display: block;
    font-family: "Cinzel", serif;
    font-weight: 500;
    font-size: 56px;
    letter-spacing: 1px;
    line-height: 1;
    margin-top: -4px;
  }
  .subtitle {
    position: absolute;
    left: 30px;
    right: 30px;
    top: 978px;
    font-family: "Noto Serif", serif;
    font-style: italic;
    font-size: 21px;
    line-height: 34px;
    letter-spacing: 0.5px;
    color: var(--ink-light);
  }
</style>
</head>
<body>
  <main class="book-cover">
    <div class="cover-art" role="img" aria-label="Illustration of a radiant woman with arms open, floating in pink and violet clouds before a golden sacred-geometry halo and a starry sky"></div>
    <p class="author-name">MIRA HOLTBY</p>
    <h1 class="title">
      <span class="title-script title-lead">The Path of</span>
      <span class="title-key">RISING</span>
      <span class="title-script title-join">The</span>
      <span class="title-name">HEART WEAVER</span>
    </h1>
    <p class="subtitle">A Quiet Path of Finding Your Voice,<br>Honoring Your Flame, and Living Your Calling.</p>
  </main>
</body>
</html>
```